We are a local Communty Pharmacy wishing to promote and market a specialised Pharmaceutical Service

We would like a design that is professional and enticing ( according to the brief In attached files)
We wish to Market Compounding Pharmacy as a specialist side of our business.
We have the expertise a purpose built preparation laboratory.
The main purpose is an Internet presence that entices prospective patients to contact or visit our physical store.

Target Market(s)

Patients Medicos and Veterinary clients

Industry/Entity Type

Pharmacy

Coding

Coded - Design and coding required

Number of Pages Required

1 page

Requirements
Must have
• Clear friendly image
Nice to have
• soft enticing feel
Should not have
• No crass loud unprofessional elements

```html
<!DOCTYPE html>
<html lang="en">
<head>
<meta charset="utf-8">
<title>Mortarleaf Pharmacy – Compounding</title>
<link href="https://fonts.googleapis.com/css2?family=Open+Sans:wght@400;600;700;800&display=swap" rel="stylesheet">
<style>
:root{
  --teal:#2fb3d3;
  --teal-dark:#1f9cbc;
  --orange:#f0892e;
  --ink:#333940;
  --muted:#7b8188;
  --line:#e6e8ea;
  --white:#ffffff;
  --footer:#2e3134;
  --footer-deep:#26292b;
  --hero-a:#e9e6e1;
  --hero-b:#c9c2b8;
}
*{box-sizing:border-box;margin:0;padding:0}
html,body{width:833px;height:1200px;overflow:hidden}
body{font-family:"Open Sans",Arial,sans-serif;color:var(--ink);background:var(--white);position:relative}

.topbar{height:24px;border-bottom:1px solid var(--line);display:flex;align-items:center;justify-content:space-between;padding:0 90px;font-size:8px;color:var(--muted)}
.social{display:flex;gap:10px}
.social span{width:9px;height:9px;border-radius:50%;background:var(--teal)}
.contact-line{display:flex;gap:16px;align-items:center}
.contact-line span{display:flex;align-items:center;gap:4px}

.header{height:52px;display:flex;align-items:center;justify-content:space-between;padding:0 90px}
.brand{display:flex;align-items:center;gap:8px;font-weight:800;font-size:15px;color:var(--teal-dark);text-transform:uppercase;letter-spacing:.3px}
.brand i{width:12px;height:12px;background:var(--teal);display:block}
.nav{display:flex;align-items:center;gap:20px;font-size:8px;font-weight:600;color:var(--ink)}
.search{width:22px;height:22px;background:var(--teal);display:flex;align-items:center;justify-content:center}

.hero{position:relative;height:292px;background:linear-gradient(110deg,var(--hero-a) 0%,#f4f2ef 45%,var(--hero-b) 100%)}
.hero-title{position:absolute;left:0;top:160px;background:rgba(255,255,255,.88);padding:10px 40px 12px 90px}
.hero-title h1{font-size:25px;font-weight:800;text-transform:uppercase;line-height:1;color:var(--ink)}
.hero-title h1 em{font-style:normal;color:var(--teal)}
.hero-title p{font-size:13px;font-weight:700;text-transform:uppercase;margin-top:4px;color:var(--ink)}
.dots{position:absolute;bottom:-18px;left:50%;transform:translateX(-50%);display:flex;gap:5px}
.dots span{width:6px;height:6px;border-radius:50%;background:#c8ccd0}
.dots span.on{background:var(--teal)}

.help{padding:34px 90px 0;text-align:center}
.help h2{font-size:17px;font-weight:800;text-transform:uppercase}
.help .lead{font-size:8px;color:var(--muted);margin-top:4px}
.features{display:grid;grid-template-columns:repeat(3,1fr);column-gap:34px;row-gap:22px;margin-top:24px}
.feature{text-align:center}
.feature svg{display:block;margin:0 auto 6px}
.feature h3{font-size:8px;font-weight:700;color:var(--orange);text-transform:uppercase}
.feature p{font-size:7px;color:var(--muted);line-height:1.5;margin-top:4px}

.about{position:relative;margin-top:26px;height:168px;background:var(--teal);color:var(--white);padding:26px 90px 0}
.about h2{font-size:17px;font-weight:800;text-transform:uppercase}
.about p{font-size:7.5px;line-height:1.6;width:440px;margin-top:10px;opacity:.95}
.btn{position:absolute;left:450px;top:118px;background:var(--ink);color:var(--white);font-size:8px;padding:6px 14px}
.about .person{position:absolute;right:90px;bottom:0;width:130px;height:190px;background:linear-gradient(180deg,#f3f5f6,#d9e4ea);border-radius:4px 4px 0 0}

.map{height:248px;background:linear-gradient(135deg,#e7ebe3 0%,#dfe5dc 55%,#b9d6e6 100%);position:relative}
.map svg{position:absolute;left:405px;top:100px}

.footer{background:var(--footer);height:134px;color:#b8bcc0;text-align:center;font-size:8px}
.footer .copy{padding-top:48px;text-transform:uppercase;letter-spacing:.5px}
.footer nav{display:flex;justify-content:center;gap:26px;margin-top:18px;font-weight:600;color:var(--white)}
.footer nav .active{color:var(--teal)}
.footer-base{position:absolute;left:0;bottom:0;width:100%;height:14px;background:var(--footer-deep)}
</style>
</head>
<body>

<div class="topbar">
  <div class="social"><span></span><span></span><span></span><span></span></div>
  <div class="contact-line">
    <span><svg width="8" height="8" viewBox="0 0 10 10"><path d="M2 1l2 2-1 1.5c.7 1.3 1.5 2 2.5 2.5L7 6l2 2-1.5 1.5C4.5 9 1 5.5.5 2.5z" fill="#2fb3d3"/></svg>+61 3 5550 1284</span>
    <span><svg width="9" height="7" viewBox="0 0 10 8"><rect x=".5" y=".5" width="9" height="7" fill="none" stroke="#2fb3d3"/><path d="M.5 .5L5 4.5 9.5.5" fill="none" stroke="#2fb3d3"/></svg>info@mortarleafpharmacy.com</span>
  </div>
</div>

<header class="header">
  <div class="brand"><i></i>Mortarleaf Pharmacy</div>
  <nav class="nav">
    <span>HOME</span><span>COMPOUNDING PHARMACY</span><span>SERVICES</span><span>LINKS</span><span>NEWS</span><span>CONTACT</span>
    <span class="search"><svg width="10" height="10" viewBox="0 0 10 10"><circle cx="4" cy="4" r="3" fill="none" stroke="#fff" stroke-width="1.4"/><path d="M6.3 6.3L9 9" stroke="#fff" stroke-width="1.4"/></svg></span>
  </nav>
</header>

<section class="hero" role="img" aria-label="Photograph of a white mortar and pestle with herbs on a light wooden bench">
  <div class="hero-title">
    <h1>Compounding <em>Preparing</em></h1>
    <p>Customised medications for patients</p>
  </div>
  <div class="dots"><span class="on"></span><span></span><span></span></div>
</section>

<section class="help">
  <h2>How can compounding help?</h2>
  <p class="lead">Almost any kind of prescription can be compounded for a specific patient requiring unique doses or delivery forms.</p>
  <div class="features">
    <div class="feature">
      <svg width="30" height="30" viewBox="0 0 30 30"><circle cx="15" cy="15" r="13" fill="none" stroke="#2fb3d3" stroke-width="1.5"/><circle cx="15" cy="11" r="3.5" fill="#2fb3d3"/><path d="M9 22c1-4 11-4 12 0z" fill="#2fb3d3"/></svg>
      <h3>Children</h3>
      <p>We can add a flavour to the medicine to make an unpleasant taste more palatable, or blend it with a favourite treat.</p>
    </div>
    <div class="feature">
      <svg width="30" height="30" viewBox="0 0 30 30"><circle cx="15" cy="15" r="13" fill="none" stroke="#2fb3d3" stroke-width="1.5"/><rect x="9" y="12" width="12" height="6" rx="3" fill="#2fb3d3"/></svg>
      <h3>Appetite Sufferers</h3>
      <p>Some medicines are hard to swallow, so we can prepare liquids, gels or lozenges that are easier to take each day.</p>
    </div>
    <div class="feature">
      <svg width="30" height="30" viewBox="0 0 30 30"><circle cx="15" cy="15" r="13" fill="none" stroke="#2fb3d3" stroke-width="1.5"/><circle cx="15" cy="12" r="4" fill="none" stroke="#2fb3d3" stroke-width="1.6"/><path d="M15 16v6M12 19.5h6" stroke="#2fb3d3" stroke-width="1.6"/></svg>
      <h3>Women's Health</h3>
      <p>Hormone replacement therapy can be tailored to your body, with creams and capsules matched to your own needs.</p>
    </div>
    <div class="feature">
      <svg width="30" height="30" viewBox="0 0 30 30"><circle cx="15" cy="15" r="13" fill="none" stroke="#2fb3d3" stroke-width="1.5"/><path d="M9 17l4 4 8-10" fill="none" stroke="#2fb3d3" stroke-width="2"/></svg>
      <h3>Thyroid Treatment</h3>
      <p>We can assist your doctor's prescribing with slow release thyroid preparations made in exact strengths for you.</p>
    </div>
    <div class="feature">
      <svg width="30" height="30" viewBox="0 0 30 30"><circle cx="15" cy="15" r="13" fill="none" stroke="#2fb3d3" stroke-width="1.5"/><path d="M15 8v14M8 15h14" stroke="#2fb3d3" stroke-width="2"/></svg>
      <h3>Allergies</h3>
      <p>Many commercial products contain fillers or dyes; we prepare versions free of the ingredients that trouble you.</p>
    </div>
    <div class="feature">
      <svg width="30" height="30" viewBox="0 0 30 30"><circle cx="15" cy="15" r="13" fill="none" stroke="#2fb3d3" stroke-width="1.5"/><path d="M10 20c0-7 5-11 11-11-1 7-5 11-11 11z" fill="#2fb3d3"/></svg>
      <h3>Special Dietary Requirements</h3>
      <p>If you are vegetarian, vegan or avoid certain animal products, we can prepare medicines that respect your choices.</p>
    </div>
  </div>
</section>

<section class="about">
  <h2>What is compounding pharmacy?</h2>
  <p>When you fill a prescription, the practice of compounding creates medicine shaped around one patient. Our pharmacists work with your doctor to prepare the right strength and form in our purpose built laboratory, so every dose suits you.</p>
  <span class="btn">Read More</span>
  <div class="person" role="img" aria-label="Photograph of a smiling pharmacist in a white coat with arms folded"></div>
</section>

<section class="map" role="img" aria-label="Street map showing the pharmacy location beside the river">
  <svg width="20" height="28" viewBox="0 0 20 28"><path d="M10 27C4 18 1 14 1 9.5a9 9 0 0118 0C19 14 16 18 10 27z" fill="#333940"/><circle cx="10" cy="9.5" r="3.5" fill="#fff"/></svg>
</section>

<footer class="footer">
  <p class="copy">Mortarleaf Pharmacy 2024. All rights reserved.</p>
  <nav><span>HOME</span><span>COMPOUNDING PHARMACY</span><span class="active">SERVICES</span><span>LINKS</span><span>NEWS</span><span>CONTACT</span></nav>
  <div class="footer-base"></div>
</footer>

</body>
</html>
```